Sign Design

We already have a logo, but would like to design 2 x signs.
Sign 1:
Dimensions 1500mm wide x 2500m high.
Information to include on sign: - Clinic name and logo (attached)
- the word "DENTIST "
- Street number (which is 348)
Phone number (which is 6153 4097)

Sign 2:
Dimensions: 800mm wide x 600mm high

```html
<!DOCTYPE html>
<html lang="en">
<head>
<meta charset="utf-8">
<title>Kellbrook Dental Care – Sign</title>
<link href="https://fonts.googleapis.com/css2?family=Arimo:wght@400;700&display=swap" rel="stylesheet">
<style>
  :root {
    --brand-dark: #136f37;
    --brand-tint: #def3b2;
    --paper: #ffffff;
  }
  html, body {
    margin: 0;
    padding: 0;
    overflow: hidden;
    background: var(--paper);
  }
  .sign {
    position: relative;
    width: 1036px;
    height: 1200px;
    background: var(--paper);
    font-family: "Arimo", Arial, sans-serif;
    color: var(--brand-dark);
    overflow: hidden;
  }
  .brand-mark {
    position: absolute;
    left: 95px;
    top: 300px;
    width: 240px;
    height: 240px;
    border-radius: 50%;
    background: var(--brand-tint);
  }
  .brand-name {
    position: absolute;
    margin: 0;
    font-weight: 400;
    line-height: 1;
    white-space: nowrap;
    color: var(--brand-dark);
  }
  .brand-name--primary {
    left: 380px;
    top: 317px;
    font-size: 118px;
    letter-spacing: -3px;
  }
  .brand-name--secondary {
    left: 584px;
    top: 426px;
    font-size: 70px;
    letter-spacing: -1px;
  }
  .divider {
    position: absolute;
    left: 246px;
    top: 638px;
    width: 6px;
    height: 357px;
    background: var(--brand-dark);
  }
  .info {
    position: absolute;
    margin: 0;
    line-height: 1;
    white-space: nowrap;
  }
  .info--title {
    left: 298px;
    top: 658px;
    font-size: 115px;
    font-weight: 700;
    letter-spacing: 1px;
  }
  .info--street {
    left: 302px;
    top: 785px;
    font-size: 72px;
    font-weight: 400;
  }
  .info--phone {
    left: 299px;
    top: 888px;
    font-size: 75px;
    font-weight: 400;
  }
</style>
</head>
<body>
  <main class="sign">
    <div class="brand-mark" aria-hidden="true"></div>
    <p class="brand-name brand-name--primary">Kellbrook</p>
    <p class="brand-name brand-name--secondary">Dental Care</p>
    <div class="divider" aria-hidden="true"></div>
    <h1 class="info info--title">DENTIST</h1>
    <p class="info info--street">Street no : 348</p>
    <p class="info info--phone">Ph no : 6153 4097</p>
  </main>
</body>
</html>
```